Produkt-Etiketten-Design für Wagyu-Bolognese-Sauce
Zielgruppe
Wir sind ein landwirtschaftliches Unternehmen und züchten Wagyu Rinder und betreiben einen Online Shop.
Unsere Produktpallete beinhaltet Tk und frisch Fleisch und nun wollen wir unser Palette um Convinienc Food erweitern und dafür brauchen wir Etiketten.
Aufgabenstellung
Es sollte optisch zu unserem webauftritt und unserer Linie passen.
Wir brauchen Produkt Etikett für Wagyu Bolognese Sauce.
Gläser Maße hier entnehmen - https://www.glasorbo.com/sturzglas-435ml-weissglas-mdg.-to82-karton-64stk.html
Wir bauchen auch eine Zutaten-und Nährwerttabelle

```html
<!DOCTYPE html>
<html lang="de">
<head>
<meta charset="utf-8">
<title>Lindhof Farm – Wagyu-Sauce alla Bolognese Etikett</title>
<link rel="stylesheet" href="https://fonts.googleapis.com/css2?family=Arimo:wght@400;700&family=Montserrat:wght@300;400;600&family=Fjalla+One&family=Oswald:wght@300;400&display=swap">
<style>
  :root{
    --brand-red:#a50d26;
    --ink:#4a4a4a;
    --grey-text:#6e6e6e;
    --row-grey:#b3b3b3;
    --paper:#ffffff;
    --panel:#ececec;
    --sketch-a:#d9d9d9;
    --sketch-b:#f4f4f4;
  }
  *{box-sizing:border-box;margin:0;padding:0}
  html,body{width:968px;height:1200px;overflow:hidden;background:var(--paper)}
  .canvas{position:relative;width:968px;height:1200px;background:var(--paper)}

  /* Lid sticker */
  .lid-sticker{position:absolute;left:333px;top:84px;width:262px;height:262px;border-radius:50%;background:var(--brand-red)}
  .lid-face{position:absolute;left:10px;top:10px;width:242px;height:242px;border-radius:50%;background:var(--paper);overflow:hidden}
  .lid-face .sketch{position:absolute;left:30px;top:28px;width:182px;height:190px;border-radius:40% 40% 30% 30%;background:radial-gradient(circle at 50% 45%,var(--sketch-a),var(--sketch-b) 70%)}
  .lid-tab{position:absolute;left:430px;top:330px;width:70px;height:252px;background:var(--brand-red);color:var(--paper);font-family:"Oswald",sans-serif;font-weight:300;font-size:8px;line-height:11px;text-align:center;padding-top:106px}
  .tab-icon{display:block;margin:0 auto 4px}
  .tab-claim{display:block;margin-bottom:12px}

  /* Wrap label */
  .wrap-label{position:absolute;left:27px;top:597px;width:874px;height:335px;background:var(--paper)}
  .band-top{position:absolute;left:0;top:0;width:100%;height:13px;background:var(--brand-red)}
  .band-bottom{position:absolute;left:0;bottom:0;width:100%;height:45px;background:var(--brand-red);display:flex;align-items:center;justify-content:center}
  .product-name{font-family:"Fjalla One",sans-serif;color:var(--paper);font-size:31px;letter-spacing:-0.3px;line-height:45px}
  .product-name small{font-size:20px}
  .center-panel{position:absolute;left:252px;top:13px;width:371px;height:277px;background:var(--panel)}
  .brand-name{position:absolute;left:0;top:2px;width:100%;text-align:center;font-family:"Fjalla One",sans-serif;font-size:40px;line-height:46px;color:var(--brand-red);letter-spacing:.5px}
  .center-panel .sketch{position:absolute;left:52px;top:56px;width:267px;height:221px;border-radius:40% 40% 20% 20%;background:radial-gradient(circle at 50% 45%,var(--sketch-a),var(--panel) 70%)}

  .info-left{position:absolute;left:12px;top:17px;width:226px;font-family:"Arimo",sans-serif;color:var(--ink);text-align:center}
  .tagline{font-weight:700;font-size:14px;line-height:17px;white-space:nowrap}
  .ingredients{margin-top:12px;font-size:11.5px;line-height:14.5px}
  .nutrition{margin-top:12px;width:226px;border-collapse:collapse;font-size:10.8px;text-align:left}
  .nutrition th{background:var(--row-grey);font-weight:700;text-align:center;height:14px;line-height:14px}
  .nutrition td{height:14px;line-height:14px;padding:0}
  .nutrition td:last-child{text-align:right}
  .nutrition tr.shade td{background:var(--row-grey)}
  .nutrition .indent{padding-left:7px}

  .info-right{position:absolute;left:636px;top:17px;width:226px;font-family:"Montserrat",sans-serif;color:var(--grey-text);text-align:center}
  .best-before{font-weight:600;font-size:13px;line-height:17px}
  .batch{margin-top:17px;font-weight:600;font-size:13px}
  .storage{margin-top:18px;font-weight:300;font-size:14px;line-height:17px}
  .volume{margin-top:32px;font-weight:600;font-size:25px;color:#5d5d5d}
  .producer{margin-top:34px;font-weight:300;font-size:14px;line-height:17px}
</style>
</head>
<body>
<div class="canvas">

  <div class="lid-sticker">
    <div class="lid-face">
      <div class="sketch" role="img" aria-label="Feine graue Linienzeichnung eines Wagyu-Rinderkopfes"></div>
    </div>
  </div>
  <div class="lid-tab">
    <svg class="tab-icon" width="34" height="30" viewBox="0 0 34 30" aria-hidden="true">
      <path d="M4 27 C10 18 18 12 27 6 M8 22 C6 12 14 4 30 3 C31 14 24 23 10 23" fill="none" stroke="#fff" stroke-width="1.6" stroke-linecap="round"/>
    </svg>
    <span class="tab-claim">Nur sicheres<br>und gesundes Futter</span>
    <svg class="tab-icon" width="30" height="30" viewBox="0 0 30 30" aria-hidden="true">
      <circle cx="15" cy="15" r="12.5" fill="none" stroke="#fff" stroke-width="2"/>
      <path d="M9 15.5 L13.5 20 L21.5 10.5" fill="none" stroke="#fff" stroke-width="2.2" stroke-linecap="round" stroke-linejoin="round"/>
    </svg>
    <span class="tab-claim">Artgerechte<br>Haltung, natürliche<br>Aufzucht</span>
  </div>

  <div class="wrap-label">
    <div class="band-top"></div>

    <div class="center-panel">
      <div class="brand-name">LINDHOF FARM</div>
      <div class="sketch" role="img" aria-label="Feine graue Linienzeichnung eines Wagyu-Rinderkopfes"></div>
    </div>

    <div class="info-left">
      <p class="tagline">Leckere Sauce nach Bologneser<br>Art aus sonnengereiften Tomaten<br>und reichlichem Fleischanteil<br>vom Wagyu-Rind</p>
      <p class="ingredients"><b>Zutaten:</b> Weiches Quellwasser, Sojaboh-<br>nen, Weizen, Meersalz, Aspergillus</p>
      <table class="nutrition">
        <tr><th colspan="2">Durchschnittsnährwerte pro 100ml</th></tr>
        <tr><td>Brennwert</td><td>111 kcal/470kj</td></tr>
        <tr class="shade"><td>Fett</td><td>0,1g</td></tr>
        <tr><td class="indent">davon ungesättigte</td><td>0,1 g</td></tr>
        <tr class="shade"><td>Fettsäuren</td><td>0,1g</td></tr>
        <tr><td>Kohlenhydrate</td><td>4,5g</td></tr>
        <tr class="shade"><td class="indent">davon Zucker</td><td>1,5g</td></tr>
        <tr><td>Protein</td><td>15,1g</td></tr>
        <tr class="shade"><td>Salz</td><td>13,8g</td></tr>
      </table>
    </div>

    <div class="info-right">
      <p class="best-before">Mindestens haltbar bis Ende:<br>12.2022</p>
      <p class="batch">Chargennummer 12-3456</p>
      <p class="storage">Nach dem Öffnen im<br>Kühlschrank aufbewahren</p>
      <p class="volume">500ml</p>
      <p class="producer">Lindhof Farm Kft<br>Feldweg 12/4<br>8841 Rosental/Ungarn</p>
    </div>

    <div class="band-bottom">
      <span class="product-name">WAGYU-SAUCE <small>alla</small> BOLOGNESE</span>
    </div>
  </div>

</div>
</body>
</html>
```